Im want a website LIKE KMT's and FleetStride.com's with product payment options like Wendaro's

I need a website LIKE KMT with a header made EXACTLY LIKE THAT OF FLEETSTRIDES .

The front page photo should be like that of FLEETSTRIDE's webpage as well.

The name of the website will be called "C.M. (Calmira Mesa)".

We will be targeting ALL MARKETS in a small town in central Panama and charging businesses "listing fees" like a phone book does but also providing informational blogs, news, and other interesting activities.

THIS IS A MULTI PAGE WEBSITE

THIS IS WHERE KMT's website meets Norvex/FleetStride.

Once the layout is built I will tweak and modify, add information, and upload items for sale.

Here is a list of specific categories that should be listed out above the front page header image/search bar

-- Home -- News -- Travel -- Activities -- Shop & Dine -- Store -- More... --

These categories should be spread across the bottom of the page in three sections:

WHATS SO GREAT ABOUT (Calmira Mesa),
HAND PICKED TOURS
ACTIVITIES etc.

Also lets use www.Wendaro.example 's
"HOT DESTINATIONS"
"BEAT THE BEST PRICES IN BOQUETE"
"OCTOBERS INSIDER PICKS"
"TOP DESTINATIONS"
and spread them in four sections side-by-side near the bottom of the page.

Overall I would like to see the finished product to be something LIKE KMT's and FleetStrides.

WE NEED ONLINE PAYMENT OPTIONS LIKE NORVEX'S WEBSITE HAS

This will be a desktop website but should be very mobile friendly as well.

-rodwell

P.S. Good luck!
Updates

If it isn't already too late to change the website name, the name of the website should be "Calmira Mesa". Added Friday, October 9, 2015

What do you guys think the budget should be to win this? Added Saturday, October 10, 2015

www.lunaverde.example is the most amazing simple site. Whoever can make me a replica with my specifications will win immediately!!!! Added Sunday, October 18, 2015

OMG www.lunaverde.example is the bomb!So simple and elegant. Whoever can make me an EXACT REPLICA OF WWW.LUNAVERDE.EXAMPLE as my site with the specifications mentioned in my brief will take home the $825.00 immediately! Good luck amigos! Added Sunday, October 18, 2015

Does anybody know how to add recurring monthly billing options on this website? Added Sunday, October 18, 2015

Target Market(s)

ALL MARKETS

Industry/Entity Type

Product

Coding

Coded - Design and coding required

Number of Pages Required

5+ page

Requirements
Must have
• Coinlark payment options.
• I must be able to add and remove photos/text and video from the HTML files in the page.
• Be creative my friends, and may the odds be forever in your favor!
Nice to have
• I added some photos of a good layout for our page below.

```html
<!DOCTYPE html>
<html lang="en">
<head>
<meta charset="utf-8">
<title>Calmira Mesa</title>
<link href="https://fonts.googleapis.com/css2?family=Roboto:wght@300;400;500;700&display=swap" rel="stylesheet">
<style>
:root{
  --blue:#1f97db;
  --blue-nav:#1783c4;
  --blue-dark:#1679b6;
  --card-blue:#2aa3de;
  --green:#3cc13b;
  --ink:#2a2f33;
  --muted:#7b848a;
  --line:#e2e6e9;
  --footer:#0f3945;
  --footer-deep:#0b2d37;
  --white:#ffffff;
}
*{box-sizing:border-box;margin:0;padding:0}
html,body{width:1200px;height:2688px;overflow:hidden}
body{font-family:'Roboto',Arial,sans-serif;color:var(--ink);background:var(--white);position:relative}
.wrap{width:864px;margin:0 auto;position:relative}
ul{list-style:none}
.block{position:absolute;left:0;width:1200px}

/* header band with navigation and newsletter */
.site-header{top:0;height:200px;background:var(--blue)}
.main-nav{height:32px;background:var(--blue-nav)}
.main-nav .wrap{display:flex;align-items:center;height:32px;gap:26px}
.brand{color:var(--white);font-size:13px;font-weight:700;margin-right:auto}
.main-nav a{color:var(--white);font-size:11px;font-weight:500;text-decoration:none}
.header-body{display:flex;justify-content:space-between;padding-top:12px}
.newsletter h3{color:var(--white);font-size:17px;font-weight:700;margin-bottom:6px}
.newsletter p{color:#d7ecfa;font-size:10px;margin-bottom:8px;width:330px}
.newsletter .field{width:300px;height:22px;background:var(--white);border-radius:2px;margin-bottom:6px;font-size:10px;color:#9aa3a8;padding:5px 8px}
.btn{display:inline-block;background:var(--green);color:var(--white);font-size:11px;font-weight:500;padding:6px 16px;border-radius:2px}
.ads{display:grid;grid-template-columns:200px 200px;gap:8px}
.ad{height:64px;border-radius:2px;padding:8px;color:var(--white);font-size:11px;font-weight:700}
.ad.a1{background:linear-gradient(90deg,#1b2a4d,#c0392b)}
.ad.a2{background:linear-gradient(90deg,#f2f2f2,#e34b3c);color:#c0392b}
.ad.a3{background:linear-gradient(90deg,#101010,#3a2c20)}
.ad.a4{background:linear-gradient(90deg,#3f86c6,#f3c44d)}

/* section headings */
.section-title{display:flex;align-items:center;gap:18px;justify-content:center;font-size:19px;font-weight:500;color:var(--ink);height:80px}
.section-title::before,.section-title::after{content:"";height:1px;width:330px;background:var(--line)}

/* shop and dine */
.shop{top:208px}
.shop-grid{display:grid;grid-template-columns:repeat(3,1fr);gap:16px}
.tile{border-radius:2px;display:flex;align-items:flex-end;padding:12px}
.tile span{color:var(--white);font-size:12px;font-weight:500}
.tile.t1,.tile.t2,.tile.t3{height:200px}
.tile.t4,.tile.t5,.tile.t6{height:192px}
.t1{background:linear-gradient(135deg,#e7a03c,#b7352c 55%,#3d6b2c)}
.t2{background:linear-gradient(135deg,#2f8c7e,#1f6f67);align-items:center!important;justify-content:center}
.t3{background:linear-gradient(135deg,#d8a062,#8f5a33 60%,#e9d7b8)}
.t4{background:linear-gradient(160deg,#6fa7c9,#e58a2f 55%,#c9651c)}
.t5{background:linear-gradient(160deg,#eef1f3,#a9b3ba 60%,#5e6a72)}
.t6{background:linear-gradient(160deg,#c9b08a,#e3c98d 50%,#6e5a44)}

/* events hero band */
.events{top:744px;height:304px;background:linear-gradient(180deg,#3f4f8a 0%,#b96a79 28%,#e7a263 45%,#3d7fb0 60%,#1d5a86 100%)}
.events .wrap{display:flex;padding-top:20px}
.events-intro{width:290px;color:var(--white)}
.events-intro h2{font-size:26px;font-weight:500;margin-bottom:6px}
.events-intro p{font-size:11px;line-height:1.45}
.events-cats{width:150px;color:var(--white);font-size:11px;line-height:20px}
.events-cats li::before{content:"";display:inline-block;width:6px;height:6px;background:var(--white);margin-right:7px}
.events-list{flex:1;color:var(--white)}
.event{display:flex;gap:10px;align-items:center;margin-bottom:14px}
.date{width:32px;height:32px;border:1px solid var(--white);font-size:13px;font-weight:700;display:flex;align-items:center;justify-content:center;flex:none}
.event b{display:block;font-size:12px}
.event small{font-size:10px;opacity:.85}

/* featured */
.featured{top:1112px}
.cards{display:grid;grid-template-columns:repeat(3,276px);gap:48px 18px}
.card{height:320px}
.card-head{height:30px;background:var(--card-blue);color:var(--white);font-size:12px;padding:8px 10px;position:relative}
.card-head i{position:absolute;right:0;top:0;width:30px;height:30px;background:var(--blue-dark);font-style:normal;text-align:center;line-height:30px;font-weight:700}
.card-img{height:140px}
.c1{background:linear-gradient(180deg,#9ec7e5,#b9a36e 60%,#6f7f3d)}
.c2{background:linear-gradient(180deg,#6ab6e5,#dfeaf2 55%,#2f86b8)}
.c3{background:linear-gradient(180deg,#5d93c4,#dce7ef 50%,#3c5f3a)}
.c4{background:linear-gradient(180deg,#7cc3ea,#3a93c9 60%,#e4d3a6)}
.c5{background:linear-gradient(180deg,#3a6fb0,#e7a35b 55%,#b44b2f)}
.c6{background:linear-gradient(180deg,#e9c17a,#9fb7cf 55%,#51708a)}
.card h4{font-size:17px;font-weight:400;line-height:1.25;margin:10px 0 6px;width:230px}
.card li,.story-side li{font-size:9px;color:var(--muted);padding:5px 0 5px 12px;border-bottom:1px solid var(--line);position:relative}
.card li::before,.story-side li::before{content:"";position:absolute;left:0;top:9px;width:4px;height:4px;background:var(--ink)}

/* top stories */
.stories{top:1912px}
.stories h3{font-size:14px;font-weight:500;margin-bottom:10px}
.stories-row{display:flex;gap:20px}
.story-side{width:272px}
.side-img{height:150px;background:linear-gradient(180deg,#8cc6e8,#e7d7a8 60%,#4b8a4e)}
.story-side h4{font-size:15px;font-weight:400;line-height:1.3;margin:8px 0 6px}
.story-side .btn{display:block;text-align:center;margin-top:12px}
.story-main{flex:1;height:330px;position:relative;background:linear-gradient(180deg,#7fb2d8,#dbe8ee 50%,#3f7fa8 80%,#1f4e6e)}
.story-caption{position:absolute;left:0;right:0;bottom:0;padding:14px 16px;background:linear-gradient(0deg,rgba(0,0,0,.7),rgba(0,0,0,0));color:var(--white)}
.story-caption h2{font-size:27px;font-weight:500}
.story-caption p{font-size:10px;opacity:.9}

/* footer */
.site-footer{top:2372px;height:316px;background:var(--footer)}
.footer-top{display:flex;justify-content:space-between;align-items:center;padding-top:16px}
.footer-top h2{color:var(--white);font-size:15px;font-weight:500}
.search{width:200px;height:22px;background:#e9eef0;border-radius:2px;font-size:10px;color:#8a9499;padding:5px 8px}
.footer-cols{display:flex;gap:32px;margin-top:22px}
.footer-cols h5{color:var(--white);font-size:9px;font-weight:700;margin-bottom:8px}
.footer-cols li{color:#9fb6bd;font-size:8px;line-height:15px}
.footer-cols .double ul{columns:2;column-gap:18px}
.footer-bottom{position:absolute;bottom:0;left:0;width:1200px;height:44px;background:var(--footer-deep)}
.footer-bottom .wrap{display:flex;justify-content:space-between;align-items:center;height:44px;color:#9fb6bd;font-size:8px}
.social{display:flex;gap:6px}
.social span{width:16px;height:16px;border-radius:50%;background:#2a8fc4}
.pay{display:flex;gap:5px}
.pay span{width:24px;height:15px;background:#dfe6e9;border-radius:2px}
</style>
</head>
<body>

<header class="block site-header">
  <nav class="main-nav">
    <div class="wrap">
      <span class="brand">Calmira Mesa</span>
      <a href="#">Home</a><a href="#">News</a><a href="#">Travel</a><a href="#">Activities</a><a href="#">Shop &amp; Dine</a><a href="#">Store</a><a href="#">More...</a>
    </div>
  </nav>
  <div class="wrap header-body">
    <div class="newsletter">
      <h3>Email Newsletter</h3>
      <p>Join our newsletter and get the latest local deals and news</p>
      <div class="field">Your Name</div>
      <div class="field">Your Email</div>
      <span class="btn">Subscribe</span>
    </div>
    <div class="ads">
      <div class="ad a1" role="img" aria-label="Advertisement banner">Paradise Getaway</div>
      <div class="ad a2" role="img" aria-label="Advertisement banner">25% Off</div>
      <div class="ad a3" role="img" aria-label="Advertisement banner">Big Deals Today</div>
      <div class="ad a4" role="img" aria-label="Advertisement banner">Summer Sale</div>
    </div>
  </div>
</header>

<section class="block shop">
  <div class="wrap">
    <h2 class="section-title">Shop &amp; Dine</h2>
    <div class="shop-grid">
      <div class="tile t1" role="img" aria-label="Fresh tropical fruit platter"><span>Fresh Fruit Market</span></div>
      <div class="tile t2" role="img" aria-label="Teal dining promotion"><span>Local Dining Guide</span></div>
      <div class="tile t3" role="img" aria-label="Plated food dish"><span>Cafe of the Week</span></div>
      <div class="tile t4" role="img" aria-label="Tropical drink at sunset"><span>Local Drink Spots</span></div>
      <div class="tile t5" role="img" aria-label="Shopper in a store"><span>Shopping Deals</span></div>
      <div class="tile t6" role="img" aria-label="Baked pastries"><span>Bakery Favourites</span></div>
    </div>
  </div>
</section>

<section class="block events" role="img" aria-label="Ocean rocks at sunset background">
  <div class="wrap">
    <div class="events-intro">
      <h2>Upcoming Events</h2>
      <p>Here is the list of events in and around Calmira Mesa. Click to see more details.</p>
    </div>
    <ul class="events-cats">
      <li>Festivals</li><li>Special Events</li><li>Local Music</li><li>Arts</li><li>Food &amp; Drink</li><li>Just of Cruise</li>
    </ul>
    <div class="events-list">
      <div class="event"><div class="date">05</div><div><b>Coast Cuisine &amp; Wine Festival</b><small>10:00 AM &middot; Mesa Plaza</small></div></div>
      <div class="event"><div class="date">12</div><div><b>Local Music Night</b><small>7:00 PM &middot; Town Square</small></div></div>
      <div class="event"><div class="date">18</div><div><b>Coast Crafts &amp; Market Day</b><small>9:00 AM &middot; Main Street</small></div></div>
      <div class="event"><div class="date">26</div><div><b>Harvest Coffee &amp; Flower Festival</b><small>All Day &middot; Mesa Park</small></div></div>
      <span class="btn">View All Events</span>
    </div>
  </div>
</section>

<section class="block featured">
  <div class="wrap">
    <h2 class="section-title">Featured Section</h2>
    <div class="cards">
      <article class="card"><div class="card-head">Lorem Ipsum<i>1</i></div><div class="card-img c1" role="img" aria-label="Country road landscape"></div><h4>Lorem ipsum dolor sit amet esta di mora</h4><ul><li>Mesa ut enim ad minim venia quis</li><li>Duis aute irure dolor in reprehend</li><li>Excepteur sint occaecat cupidatat</li><li>Sed ut perspiciatis unde omnis iste</li></ul></article>
      <article class="card"><div class="card-head">Lorem Ipsum<i>2</i></div><div class="card-img c2" role="img" aria-label="Sailboat on the sea"></div><h4>Lorem ipsum dolor sit amet esta di mora</h4><ul><li>Mesa ut enim ad minim venia quis</li><li>Duis aute irure dolor in reprehend</li><li>Excepteur sint occaecat cupidatat</li><li>Sed ut perspiciatis unde omnis iste</li></ul></article>
      <article class="card"><div class="card-head">Lorem Ipsum<i>3</i></div><div class="card-img c3" role="img" aria-label="Mountain valley view"></div><h4>Lorem ipsum dolor sit amet esta di mora</h4><ul><li>Mesa ut enim ad minim venia quis</li><li>Duis aute irure dolor in reprehend</li><li>Excepteur sint occaecat cupidatat</li><li>Sed ut perspiciatis unde omnis iste</li></ul></article>
      <article class="card"><div class="card-head">Lorem Ipsum<i>4</i></div><div class="card-img c4" role="img" aria-label="Tropical beach"></div><h4>Lorem ipsum dolor sit amet esta di mora</h4><ul><li>Mesa ut enim ad minim venia quis</li><li>Duis aute irure dolor in reprehend</li><li>Excepteur sint occaecat cupidatat</li><li>Sed ut perspiciatis unde omnis iste</li></ul></article>
      <article class="card"><div class="card-head">Lorem Ipsum<i>5</i></div><div class="card-img c5" role="img" aria-label="Runner at sunset"></div><h4>Lorem ipsum dolor sit amet esta di mora</h4><ul><li>Mesa ut enim ad minim venia quis</li><li>Duis aute irure dolor in reprehend</li><li>Excepteur sint occaecat cupidatat</li><li>Sed ut perspiciatis unde omnis iste</li></ul></article>
      <article class="card"><div class="card-head">Lorem Ipsum<i>6</i></div><div class="card-img c6" role="img" aria-label="Coastal mountains"></div><h4>Lorem ipsum dolor sit amet esta di mora</h4><ul><li>Mesa ut enim ad minim venia quis</li><li>Duis aute irure dolor in reprehend</li><li>Excepteur sint occaecat cupidatat</li><li>Sed ut perspiciatis unde omnis iste</li></ul></article>
    </div>
  </div>
</section>

<section class="block stories">
  <div class="wrap">
    <h2 class="section-title">Top Stories</h2>
    <h3>Latest Top Stories</h3>
    <div class="stories-row">
      <div class="story-side">
        <div class="side-img" role="img" aria-label="Palm trees by a beach"></div>
        <h4>Lorem ipsum dolor sit amet esta di mora</h4>
        <ul><li>Mesa ut enim ad minim venia quis</li><li>Duis aute irure dolor in reprehend</li><li>Excepteur sint occaecat cupidatat</li><li>Sed ut perspiciatis unde omnis iste</li></ul>
        <span class="btn">Read More Stories</span>
      </div>
      <div class="story-main" role="img" aria-label="Cruise ship at a harbour">
        <div class="story-caption"><h2>Lorel ipsum dolor sit amet</h2><p>Duis aute irure dolor in reprehenderit in voluptate velit</p></div>
      </div>
    </div>
  </div>
</section>

<footer class="block site-footer">
  <div class="wrap">
    <div class="footer-top"><h2>Calmira Mesa, Panama</h2><div class="search">Search</div></div>
    <div class="footer-cols">
      <div><h5>TRAVEL</h5><ul><li>Hotels</li><li>Tours</li><li>Beaches</li><li>Hiking</li><li>Transport</li><li>Maps</li></ul></div>
      <div><h5>COMPANY</h5><ul><li>About Us</li><li>Careers</li><li>Advertise</li><li>Listings</li><li>Press</li><li>Contact</li></ul></div>
      <div><h5>FRIENDS</h5><ul><li>Partners</li><li>Blogs</li><li>Locals</li><li>Guides</li><li>Forum</li></ul></div>
      <div><h5>SUPPORT</h5><ul><li>Help Center</li><li>Payments</li><li>Billing</li><li>Privacy</li><li>Terms</li></ul></div>
      <div><h5>NEWS</h5><ul><li>Local News</li><li>Business</li><li>Weather</li><li>Sports</li><li>Culture</li></ul></div>
      <div><h5>ACTIVITIES</h5><ul><li>Rafting</li><li>Zip Lines</li><li>Coffee Tours</li><li>Fishing</li><li>Birding</li></ul></div>
      <div class="double"><h5>TOP DESTINATIONS</h5><ul><li>Hot Destinations</li><li>Best Prices</li><li>Insider Picks</li><li>Top Destinations</li><li>Hand Picked Tours</li><li>Mesa Highlands</li><li>Volcano Trail</li><li>River Valley</li><li>Old Town</li><li>Hot Springs</li></ul></div>
    </div>
  </div>
  <div class="footer-bottom">
    <div class="wrap">
      <span>&copy; 2015 All Rights Reserved</span>
      <div class="social"><span></span><span></span><span></span><span></span><span></span><span></span></div>
      <div class="pay"><span></span><span></span><span></span><span></span><span></span></div>
    </div>
  </div>
</footer>

</body>
</html>
```